Business card for biotech sales agent

I need a logo and business card designed for my company Belunor. We work in partnership with Kestrel Group. Kestrel have developed advanced biotech. Their hand sanitiser is alcohol free and works for 24 hours on skin, even with regular hand washing. The surface sanitiser works for up to 30 days on surfaces and fabrics. Its food-safe, it's non-toxic, safe for animals and humans. The products have a very wide variety of applications: everything from agri-business, hotels, hospitality, schools, child and baby care, transport, meat processing etc.<br/>I would like my design to use blues or green-blues and communicate a bit of nano-tech but also trust and safety.<br/>I would also use the Kestrel logo on my card next to 'sales & distribution agent'

Target Market(s)

B2B, selling to FMCG and large companies such as airlines

Industry/Entity Type

Biotechnology

Contact Information for Business Card

Helen Pritch
Director

Phone: +64 22 519 3064
Email: helen@belunor.co
www.belunor.co
7 Tamsin St, Newmarket, Auckland, New Zealand 1023

Font styles to use
Sans Serif

Colors
3276b5
33b8a4
34a7d8
3176b5
ffffff

Requirements
Must have
• Not be too busy, clean space is good
• A logo styling to the word Belunor
Nice to have
• A little bit of a bio-tech image as a screen perhaps

```html
<!DOCTYPE html>
<html lang="en">
<head>
<meta charset="utf-8">
<title>Belunor — Business Card</title>
<link rel="stylesheet" href="https://fonts.googleapis.com/css2?family=Open+Sans:wght@400;600&display=swap">
<style>
  :root {
    --page: #e8ecec;
    --teal-light: #2fb7a0;
    --teal-mid: #2a9c8b;
    --teal-deep: #2d7f74;
    --band: #2ba592;
    --slate: #37615f;
    --slate-edge: #33595a;
    --accent-blue: #3176b5;
    --white: #ffffff;
    --text-soft: #eef6f5;
  }
  * { box-sizing: border-box; margin: 0; padding: 0; }
  html, body {
    width: 1200px; height: 1200px; overflow: hidden;
    background: var(--page);
    font-family: "Open Sans", Arial, sans-serif;
  }
  .sheet {
    width: 1200px; height: 1200px;
    display: flex; flex-direction: column;
    align-items: center; justify-content: center; gap: 60px;
  }
  .card {
    position: relative;
    width: 900px; height: 514px;
    overflow: hidden;
    box-shadow: 0 10px 30px rgba(30, 60, 60, 0.18);
    background: linear-gradient(90deg, var(--teal-deep) 0%, var(--teal-mid) 55%, var(--teal-light) 100%);
  }
  .card__band {
    position: absolute; left: 0; right: 0; height: 26px;
    background: var(--band); z-index: 3;
  }
  .card__band--top { top: 0; }
  .card__band--bottom { bottom: 0; }
  .card__panel {
    position: absolute; inset: 0;
    background: linear-gradient(180deg, var(--slate) 0%, var(--slate-edge) 100%);
    z-index: 1;
  }
  .card__rule {
    position: absolute; top: 26px; bottom: 26px; right: 40px;
    width: 5px; background: var(--accent-blue); z-index: 4;
  }

  /* Back */
  .card--back {
    background: linear-gradient(90deg, var(--teal-light) 0%, var(--teal-mid) 60%, var(--teal-deep) 100%);
  }
  .card--back .card__panel { clip-path: polygon(38% 0, 100% 0, 100% 100%, 62% 100%); }
  .brand {
    position: absolute; z-index: 5;
    left: 0; right: 0; top: 180px;
    display: flex; align-items: center; justify-content: center; gap: 22px;
  }
  .brand__name {
    font-weight: 600; font-size: 80px; letter-spacing: 4px;
    color: var(--white); line-height: 1;
  }
  .brand__dot {
    width: 54px; height: 54px; border-radius: 50%;
    background: var(--accent-blue);
    margin-top: 8px;
  }

  /* Front */
  .card--front .card__panel { clip-path: polygon(0 0, 62% 0, 38% 100%, 0 100%); }
  .identity {
    position: absolute; z-index: 5;
    left: 42px; top: 182px;
    color: var(--text-soft);
  }
  .identity__name { font-size: 50px; font-weight: 400; line-height: 1.1; }
  .identity__role {
    font-size: 27px; letter-spacing: 6px; margin-top: 2px; margin-left: 64px;
  }
  .contact {
    position: absolute; z-index: 5;
    right: 78px; top: 100px; width: 300px;
    color: var(--text-soft); font-size: 22px;
  }
  .contact__row {
    display: flex; align-items: center; justify-content: space-between;
    height: 52px;
  }
  .contact__icon { width: 26px; height: 26px; flex: none; }
  .contact__address {
    position: absolute; right: 0; top: 176px;
    width: 360px; text-align: right; line-height: 1.4; font-size: 23px;
  }
</style>
</head>
<body>
<main class="sheet">

  <section class="card card--back" aria-label="Card back">
    <div class="card__panel"></div>
    <div class="card__band card__band--top"></div>
    <div class="card__band card__band--bottom"></div>
    <div class="card__rule"></div>
    <div class="brand">
      <span class="brand__name">Belunor</span>
      <span class="brand__dot"></span>
    </div>
  </section>

  <section class="card card--front" aria-label="Card front">
    <div class="card__panel"></div>
    <div class="card__band card__band--top"></div>
    <div class="card__band card__band--bottom"></div>
    <div class="card__rule"></div>

    <div class="identity">
      <h1 class="identity__name">Helen Pritch</h1>
      <p class="identity__role">Director</p>
    </div>

    <div class="contact">
      <div class="contact__row">
        <svg class="contact__icon" viewBox="0 0 24 24" fill="none" stroke="#eef6f5" stroke-width="1.6" stroke-linejoin="round">
          <path d="M5 3h4l2 5-2.5 1.5a11 11 0 0 0 6 6L16 13l5 2v4a2 2 0 0 1-2 2A16 16 0 0 1 3 5a2 2 0 0 1 2-2z"/>
        </svg>
        <span>+64 22 519 3064</span>
      </div>
      <div class="contact__row">
        <svg class="contact__icon" viewBox="0 0 24 24" fill="none" stroke="#eef6f5" stroke-width="1.6" stroke-linejoin="round">
          <rect x="2.5" y="5" width="19" height="14" rx="1.5"/>
          <path d="M3 6l9 7 9-7"/>
        </svg>
        <span>helen@belunor.co</span>
      </div>
      <div class="contact__row">
        <svg class="contact__icon" viewBox="0 0 24 24" fill="none" stroke="#eef6f5" stroke-width="1.6">
          <circle cx="12" cy="12" r="9.5"/>
          <ellipse cx="12" cy="12" rx="4.2" ry="9.5"/>
          <path d="M2.5 12h19M4 7h16M4 17h16"/>
        </svg>
        <span>www.belunor.co</span>
      </div>
      <p class="contact__address">7 Tamsin St, Newmarket,<br>Auckland, New Zealand 1023</p>
    </div>
  </section>

</main>
</body>
</html>
```